Graphics for website image slider

We need 4 banners for website:

We provide software development services to very small to large Businesses. The focus of these 4 banners is to portray the four steps approach to our consulting process: Assess, Analyse, Plan and Deploy

Currently we have the following on our website:
http://www.virelanq.com

We are redesigning the website and want to use 4 sliding graphics to portray the same thing, and the new site is being designed here:
http://www.virelanqonline.com/virelanq

You can use stock photos for each banner or your own creativity.

The images should be 1140px wide and about 420px High.
Updates

You can use any modern font such as google font. Not just curly fonts!

Reason: Not yet able to select the final design.

I have updated the colors and how they are supposed to flow because I noticed that some designs did not follow that (We are consultants and really want to understand our process in a powerful way):

ASSESS: Orange color (1st or 5th color above)

ANALYSE: Yellow (2nd or 6th color above)

PLAN: Green (3rd or 7th color above)

DEPLOY: Blue (4th or 8th color above)

=================================================

Some designers also made mistakes in typing the text (Please copy and paste from below):

ASSESS

We gather information and data

to identify and delineate

your central and most pressing business and IT issues.

ANALYSE

We show you exactly where you are in terms of IT maturity

using our optimization tools.

We then build an IT roadmap to help you get to the next level.

PLAN:

We identify the IT products and processes necessary to implement the solution.

We then create a detailed plan of action and technical specifications.

DEPLOY

Finally, we utilize industry best practices and repeatable development and

deployment methods to ensure efficiency and high quality results

that satisfy and bring improvement within budget and timeline.

                                   

Target Market(s)

http://www.virelanq.com

Industry/Entity Type

Software

Font styles to use
Sans Serif
Other font styles liked:
• Any other modern font (No curly fonts)

Colors
fee18a
fbf289
cadf82
86cae6
f78f20
ffc214
9aca3c
0692cd

Requirements
Must have
• Graphic should convey the message for each process

```html
<!DOCTYPE html>
<html lang="en">
<head>
<meta charset="utf-8">
<title>Analyse – Consulting Process Banner</title>
<link rel="stylesheet" href="https://fonts.googleapis.com/css2?family=Open+Sans:wght@400;500;700&display=swap">
<style>
  :root {
    --yellow: #ffc214;
    --yellow-shade: #f4b70c;
    --yellow-light: #fbd23f;
    --blue-deep: #0583cc;
    --blue-bright: #00b2f5;
    --blue-button: #0692cd;
    --blue-edge: #04679a;
    --ink: #2d2b2e;
    --white: #ffffff;
  }
  * { margin: 0; padding: 0; box-sizing: border-box; }
  html, body {
    width: 1200px;
    height: 453px;
    overflow: hidden;
    background: var(--yellow);
  }
  .banner {
    position: relative;
    width: 1200px;
    height: 453px;
    overflow: hidden;
    background: var(--yellow);
    font-family: "Open Sans", sans-serif;
  }
  .banner__backdrop {
    position: absolute;
    inset: 0;
    width: 100%;
    height: 100%;
  }
  .banner__content {
    position: absolute;
    left: 0;
    right: 0;
    top: 128px;
    display: flex;
    flex-direction: column;
    align-items: center;
    text-align: center;
  }
  .banner__title {
    font-size: 63px;
    font-weight: 500;
    line-height: 1;
    letter-spacing: 0.5px;
    color: var(--ink);
  }
  .banner__text {
    margin-top: 14px;
    width: 860px;
    font-size: 15px;
    font-weight: 700;
    line-height: 19px;
    color: var(--ink);
  }
  .banner__button {
    margin-top: 54px;
    display: inline-flex;
    align-items: center;
    justify-content: center;
    width: 210px;
    height: 54px;
    background: var(--blue-button);
    border-radius: 2px;
    box-shadow: 0 3px 0 var(--blue-edge);
    font-size: 21px;
    font-weight: 700;
    color: var(--white);
    text-decoration: none;
  }
</style>
</head>
<body>
  <section class="banner">
    <svg class="banner__backdrop" viewBox="0 0 1200 453" preserveAspectRatio="none" aria-hidden="true">
      <defs>
        <linearGradient id="corner-blue-left" x1="0" y1="0" x2="1" y2="0">
          <stop offset="0" stop-color="#0583cc"/>
          <stop offset="1" stop-color="#00b2f5"/>
        </linearGradient>
        <linearGradient id="corner-blue-right" x1="0" y1="0" x2="1" y2="0">
          <stop offset="0" stop-color="#0583cc"/>
          <stop offset="0.6" stop-color="#00b2f5"/>
        </linearGradient>
      </defs>
      <rect class="backdrop__field" width="1200" height="453" fill="#ffc214"/>
      <polygon class="backdrop__stripe" points="260,453 640,0 760,0 380,453" fill="#f4b70c" opacity="0.7"/>
      <polygon class="backdrop__stripe" points="520,453 900,0 980,0 600,453" fill="#f4b70c" opacity="0.6"/>
      <polygon class="backdrop__stripe" points="0,380 320,0 400,0 60,453 0,453" fill="#f4b70c" opacity="0.55"/>
      <polygon class="backdrop__corner backdrop__corner--top" points="0,0 195,0 0,221" fill="url(#corner-blue-left)"/>
      <polygon class="backdrop__corner backdrop__corner--bottom" points="984,453 1200,205 1200,453" fill="url(#corner-blue-right)"/>
    </svg>

    <div class="banner__content">
      <h1 class="banner__title">ANALYSE</h1>
      <p class="banner__text">We show you exactly where you are in terms of IT maturity using our optimization tools. We then build an IT roadmap to help you get to the next level.</p>
      <a class="banner__button" href="#">GET STARTED</a>
    </div>
  </section>
</body>
</html>
```